Business cards Marta Kessel Sport & Events

I need new business cards to match my new logo design for my company called "Marta Kessel Sport & Events". I'm based in Germany.
With my company, I offer different services in the context of sport.

Marta Kessel owner

Marta Kessel Sports & Events
Birkenfelder Weg 12
D-63118 Offenbach

+49 69 / 31 52 94 07
info@marta-kessel.example
www.marta-kessel.example

Contact Information for Business Card

Marta Kessel Inhaberin Marta Kessel Sport & Events Birkenfelder Weg 12 D-63118 Offenbach +49 69 / 31 52 94 07 info@marta-kessel.example www.marta-kessel.example

Requirements
Must have
• Logo | Double sided business card

```html
<!DOCTYPE html>
<html lang="de">
<head>
<meta charset="utf-8">
<title>Marta Kessel Sport &amp; Events – Visitenkarten</title>
<link rel="stylesheet" href="https://fonts.googleapis.com/css2?family=Michroma&family=Poppins:wght@400;500&display=swap">
<style>
  :root {
    --backdrop: #c9c9c9;
    --card-dark: #0e0e0e;
    --card-light: #ffffff;
    --accent: #f7a11a;
    --ink: #161616;
    --ink-soft: #2b2b2b;
    --on-dark: #ffffff;
    --faint-on-dark: #1c1c1c;
  }
  * { box-sizing: border-box; margin: 0; padding: 0; }
  html, body { width: 1200px; height: 852px; overflow: hidden; }
  body {
    background: radial-gradient(circle at 50% 45%, #e2e2e2 0%, var(--backdrop) 100%);
    position: relative;
    font-family: "Poppins", sans-serif;
  }
  .card {
    position: absolute;
    width: 560px;
    height: 320px;
    border-radius: 18px;
    overflow: hidden;
    box-shadow: 0 10px 24px rgba(0,0,0,0.22);
  }
  /* Front side */
  .card--front {
    left: 90px; top: 100px;
    background: var(--card-dark);
  }
  .front__decor {
    position: absolute;
    right: -40px; top: -50px;
    width: 300px; height: 300px;
    border-radius: 50%;
    border: 34px solid var(--faint-on-dark);
  }
  .front__brand {
    position: absolute;
    left: 0; right: 0; top: 0; bottom: 0;
    display: flex;
    align-items: center;
    justify-content: center;
    gap: 22px;
  }
  .brand__dot {
    width: 74px; height: 74px;
    border-radius: 50%;
    border: 10px solid var(--accent);
    flex: none;
  }
  .brand__name {
    font-family: "Michroma", sans-serif;
    color: var(--on-dark);
    font-size: 26px;
    line-height: 1.35;
    letter-spacing: 1px;
    text-transform: uppercase;
  }
  .brand__name span { display: block; font-size: 14px; letter-spacing: 6px; }

  /* Back side */
  .card--back {
    left: 550px; top: 450px;
    background: var(--card-light);
  }
  .back__mark {
    position: absolute;
    right: 34px; top: 36px;
    width: 220px; height: 220px;
    border-radius: 50%;
    background: var(--accent);
  }
  .back__details {
    position: absolute;
    left: 40px; top: 50px;
    color: var(--ink);
  }
  .person__name {
    font-family: "Michroma", sans-serif;
    font-size: 19px;
    letter-spacing: 0.5px;
    text-transform: uppercase;
  }
  .person__role {
    font-family: "Michroma", sans-serif;
    font-size: 11px;
    color: var(--accent);
    letter-spacing: 1.5px;
    margin-top: 4px;
    text-transform: uppercase;
  }
  .address {
    font-style: normal;
    font-size: 12.5px;
    line-height: 1.55;
    color: var(--ink-soft);
    margin-top: 52px;
  }
  .contact-list {
    list-style: none;
    margin-top: 12px;
    font-size: 12.5px;
    color: var(--ink-soft);
  }
  .contact-list li {
    display: flex;
    align-items: center;
    gap: 9px;
    line-height: 22px;
  }
  .contact-icon { width: 15px; height: 15px; flex: none; }
</style>
</head>
<body>

  <section class="card card--front" aria-label="Vorderseite">
    <div class="front__decor"></div>
    <div class="front__brand">
      <div class="brand__dot"></div>
      <p class="brand__name">Marta Kessel<span>Sport &amp; Events</span></p>
    </div>
  </section>

  <section class="card card--back" aria-label="Rückseite">
    <div class="back__mark"></div>
    <div class="back__details">
      <h1 class="person__name">Marta Kessel</h1>
      <p class="person__role">Owner</p>
      <address class="address">
        Marta Kessel Sports &amp; Events<br>
        Birkenfelder Weg 12<br>
        D-63118 Offenbach
      </address>
      <ul class="contact-list">
        <li>
          <svg class="contact-icon" viewBox="0 0 16 16" aria-hidden="true">
            <circle cx="8" cy="8" r="7" fill="none" stroke="#f7a11a" stroke-width="1.4"/>
            <path d="M5.3 4.6l1.3-.3.8 1.8-.9.7a5 5 0 0 0 2.6 2.6l.7-.9 1.8.8-.3 1.3c-3.3.3-6.3-2.7-6-6z" fill="#f7a11a"/>
          </svg>
          +49 69 / 31 52 94 07
        </li>
        <li>
          <svg class="contact-icon" viewBox="0 0 16 16" aria-hidden="true">
            <circle cx="8" cy="8" r="7" fill="none" stroke="#f7a11a" stroke-width="1.4"/>
            <rect x="4.3" y="5.3" width="7.4" height="5.4" rx="0.6" fill="none" stroke="#f7a11a" stroke-width="1.1"/>
            <path d="M4.5 5.6L8 8.3l3.5-2.7" fill="none" stroke="#f7a11a" stroke-width="1.1"/>
          </svg>
          info@marta-kessel.example
        </li>
        <li>
          <svg class="contact-icon" viewBox="0 0 16 16" aria-hidden="true">
            <circle cx="8" cy="8" r="7" fill="none" stroke="#f7a11a" stroke-width="1.4"/>
            <circle cx="8" cy="8" r="3.6" fill="none" stroke="#f7a11a" stroke-width="1"/>
            <ellipse cx="8" cy="8" rx="1.5" ry="3.6" fill="none" stroke="#f7a11a" stroke-width="0.9"/>
            <path d="M4.4 8h7.2" stroke="#f7a11a" stroke-width="0.9"/>
          </svg>
          www.marta-kessel.example
        </li>
      </ul>
    </div>
  </section>

</body>
</html>
```